Kestrel Signs Facebook Banner Design

Design a facebook banner for a sign company. I would like to have a modern approach to it.

Product Offering:
Signs
Banners
Decals
Commercial Wraps

```html
<!DOCTYPE html>
<html lang="en">
<head>
<meta charset="utf-8">
<title>Kestrel Signs – Facebook Banner</title>
<link href="https://fonts.googleapis.com/css2?family=Anton&family=Poppins:wght@600;700&display=swap" rel="stylesheet">
<style>
  :root {
    --paper: #f1f1f0;
    --paper-shade: #e4e4e2;
    --ink: #141414;
    --brand-red: #e0120f;
    --torn-red: #d8100e;
    --torn-black: #1b1b1b;
    --torn-white: #fbfbfa;
    --contact: #5b4b42;
    --photo-light: #c9c7c2;
    --photo-mid: #9d9a94;
    --photo-dark: #5e5c58;
  }
  html, body {
    margin: 0;
    padding: 0;
    width: 1200px;
    height: 444px;
    overflow: hidden;
    background: var(--paper);
  }
  .banner {
    position: relative;
    width: 1200px;
    height: 444px;
    overflow: hidden;
    background: linear-gradient(135deg, var(--paper) 0%, var(--paper-shade) 100%);
    font-family: "Poppins", Arial, sans-serif;
    color: var(--ink);
  }
  .banner__backdrop {
    position: absolute;
    inset: 0;
  }
  .banner__title {
    position: absolute;
    left: 646px;
    top: 34px;
    width: 440px;
    margin: 0;
    text-align: center;
    font-family: "Anton", Impact, sans-serif;
    font-style: italic;
    font-weight: 400;
    font-size: 54px;
    line-height: 1;
    letter-spacing: 1px;
    text-transform: uppercase;
    color: var(--brand-red);
  }
  .banner__tagline {
    position: absolute;
    left: 652px;
    top: 114px;
    margin: 0;
    font-weight: 700;
    font-size: 17.5px;
    color: var(--ink);
  }
  .offering__heading {
    position: absolute;
    left: 606px;
    top: 182px;
    margin: 0;
    font-weight: 700;
    font-size: 21px;
    color: var(--brand-red);
  }
  .offering__list {
    position: absolute;
    left: 606px;
    top: 228px;
    margin: 0;
    padding: 0;
    list-style: none;
    display: grid;
    grid-template-columns: 205px 260px;
    row-gap: 4px;
    font-weight: 700;
    font-size: 22px;
    line-height: 1.3;
  }
  .offering__item::before {
    content: "";
    display: inline-block;
    width: 7px;
    height: 7px;
    border-radius: 50%;
    background: var(--ink);
    margin: 0 16px 4px 6px;
    vertical-align: middle;
  }
  .banner__contact {
    position: absolute;
    left: 618px;
    top: 312px;
    margin: 0;
    font-family: "Anton", Impact, sans-serif;
    font-style: italic;
    font-size: 21px;
    letter-spacing: 1.2px;
    text-transform: uppercase;
    color: var(--contact);
  }
</style>
</head>
<body>
<main class="banner">
  <svg class="banner__backdrop" width="1200" height="444" viewBox="0 0 1200 444" aria-hidden="false">
    <defs>
      <linearGradient id="storefront-tone" x1="0" y1="0" x2="1" y2="1">
        <stop offset="0" stop-color="var(--photo-light)"/>
        <stop offset="0.5" stop-color="var(--photo-mid)"/>
        <stop offset="1" stop-color="var(--photo-dark)"/>
      </linearGradient>
    </defs>

    <rect class="storefront-photo" x="40" y="0" width="585" height="444" fill="url(#storefront-tone)"
          role="img" aria-label="Photo of a square black hanging shop sign mounted on a stone building wall"/>

    <polygon class="torn-strip torn-strip--edge" fill="var(--torn-white)"
      points="612,0 640,0 634,60 646,120 632,190 644,260 630,330 642,400 630,444 604,444 616,380 604,300 618,230 606,160 620,90 608,30"/>
    <polygon class="torn-strip torn-strip--bottom" fill="var(--torn-white)"
      points="40,400 120,392 220,404 330,396 440,408 540,398 625,404 625,444 40,444"/>
    <polygon class="torn-strip torn-strip--left" fill="var(--torn-white)"
      points="0,0 56,0 48,80 60,170 46,260 58,350 48,444 0,444"/>

    <polygon class="torn-paper torn-paper--black" fill="var(--torn-black)"
      points="0,0 250,0 236,40 210,78 170,110 120,140 70,168 30,180 0,184"/>

    <polygon class="torn-paper torn-paper--red" fill="var(--torn-red)"
      points="700,444 740,420 800,404 870,388 940,372 1010,352 1080,334 1140,318 1200,300 1200,444"/>
  </svg>

  <h1 class="banner__title">Kestrel Signs</h1>
  <p class="banner__tagline">Transforming Spaces with Custom Signage.</p>

  <section class="offering">
    <h2 class="offering__heading">Product Offering:</h2>
    <ul class="offering__list">
      <li class="offering__item">Signs</li>
      <li class="offering__item">Decals</li>
      <li class="offering__item">Banners</li>
      <li class="offering__item">Commercial Wraps</li>
    </ul>
  </section>

  <p class="banner__contact">Contact us for your custom sign needs!</p>
</main>
</body>
</html>
```